Business Card Design

Online clothing womens clothing store, I sell my clothing online and at the markets.

i would like the attached picture on the front of the card and the contact information on the back.

Industry/Entity Type

Business

Contact Information for Business Card

Harbor Thistle
Maren Pilcott
(Instagram symbol) _harbor_thistle_
(Facebook symbol) www.socialnook.com/harborthistleau/

W : www.harborthistle.com.au
E : info@harborthistle.com.au
P : 0478614203

```html
<!DOCTYPE html>
<html lang="en">
<head>
<meta charset="utf-8">
<title>Harbor Thistle — Business Card</title>
<link rel="stylesheet" href="https://fonts.googleapis.com/css2?family=PT+Sans:wght@400;700&display=swap">
<style>
  :root {
    --backdrop-top: #2a2a2a;
    --backdrop-bottom: #070707;
    --card-white: #ffffff;
    --card-grey: #d6d7d5;
    --ink: #111111;
    --ink-soft: #555555;
    --tab: #000000;
    --photo-mist: #e3e8e8;
    --photo-teal: #9fb8bb;
    --photo-shadow: #5a5d68;
    --logo-text: #ffffff;
  }
  * { box-sizing: border-box; margin: 0; padding: 0; }
  html, body { width: 1200px; height: 900px; overflow: hidden; }
  body {
    position: relative;
    background: linear-gradient(180deg, var(--backdrop-top) 0%, #141414 60%, var(--backdrop-bottom) 100%);
    font-family: "PT Sans", "Myriad Pro", Arial, sans-serif;
  }
  .card {
    position: absolute;
    top: 170px;
    width: 347px;
    height: 561px;
  }
  .card--contact { left: 259px; background: var(--card-white); }
  .card--front { left: 631px; background: var(--card-grey); overflow: hidden; }

  .tab {
    position: absolute;
    left: 102px;
    width: 143px;
    background: var(--tab);
  }
  .tab--top { top: 0; height: 30px; }
  .tab--bottom { bottom: 0; height: 28px; }

  .holder-name {
    position: absolute;
    top: 183px;
    left: 0; right: 0;
    text-align: center;
    font-size: 21px;
    font-weight: 700;
    color: var(--ink);
  }
  .contact-list {
    position: absolute;
    left: 0; right: 0;
    list-style: none;
    text-align: center;
    font-size: 16px;
    line-height: 20px;
    color: var(--ink-soft);
  }
  .contact-list--direct { top: 241px; }
  .contact-list--social { top: 333px; }
  .contact-list li { white-space: nowrap; }
  .icon {
    display: inline-block;
    width: 10px; height: 10px;
    margin-right: 5px;
    vertical-align: -1px;
  }
  .icon--square { background: var(--ink); border-radius: 2px; width: 11px; height: 11px; }

  .photo-band {
    position: absolute;
    top: 165px;
    left: 0;
    width: 347px;
    height: 231px;
    background:
      radial-gradient(ellipse 40% 55% at 72% 45%, rgba(90,93,104,0.85) 0%, rgba(90,93,104,0.45) 45%, rgba(90,93,104,0) 80%),
      radial-gradient(ellipse 60% 70% at 50% 30%, rgba(159,184,187,0.8) 0%, rgba(159,184,187,0) 70%),
      linear-gradient(180deg, var(--photo-mist) 0%, #c4cccd 100%);
  }
  .brand-name {
    position: absolute;
    top: 326px;
    left: 22px;
    font-size: 40px;
    font-weight: 400;
    letter-spacing: 1px;
    color: var(--logo-text);
    white-space: nowrap;
  }
</style>
</head>
<body>
  <section class="card card--contact">
    <div class="tab tab--top"></div>
    <h1 class="holder-name">Maren Pilcott</h1>
    <ul class="contact-list contact-list--direct">
      <li><svg class="icon" viewBox="0 0 10 10"><path d="M1 3.5C1 2 2.5 1.5 5 1.5S9 2 9 3.5L7.2 4 6.8 3H3.2L2.8 4Z M2.5 5h5l1 3.5h-7Z" fill="#111"/></svg>0478614203</li>
      <li><svg class="icon" viewBox="0 0 10 10"><rect x="0.5" y="2" width="9" height="6.5" fill="#111"/><path d="M0.5 2 5 5.5 9.5 2" stroke="#fff" stroke-width="1" fill="none"/></svg>info@harborthistle.com.au</li>
      <li><svg class="icon" viewBox="0 0 10 10"><path d="M4 6 6 4M3.2 4.8 1.8 6.2a1.5 1.5 0 0 0 2 2L5.2 6.8M6.8 5.2 8.2 3.8a1.5 1.5 0 0 0-2-2L4.8 3.2" stroke="#111" stroke-width="1.3" fill="none" stroke-linecap="round"/></svg>www.harborthistle.com.au</li>
    </ul>
    <ul class="contact-list contact-list--social">
      <li><span class="icon icon--square"></span> _harbor_thistle_</li>
      <li><span class="icon icon--square"></span>www.socialnook.com/harborthistleau/</li>
    </ul>
    <div class="tab tab--bottom"></div>
  </section>

  <section class="card card--front">
    <div class="photo-band" role="img" aria-label="Misty photograph of a woman in profile with smoke drifting around her hair"></div>
    <div class="brand-name">HARBOR THISTLE</div>
  </section>
</body>
</html>
```